Word template for proposals we send to clients

We want a word template designed based on the look/feel of our website. The website is www.brovexa.com.au and while we have pictures of 2 staff on the website we have pictures of other staff if required

the template will be used to send out proposals to potential clients, therefore it has to be professional, modern and compelling for someone to open

Target Market(s)

B2B

Industry/Entity Type

It Company

Font styles to use
Serif

Colors

Designer to choose colors to be used in the design.

Requirements
Must have
• Same look and feel as website
Nice to have
• Dont know what I am missing so anythign you feel i need to add

```html
<!DOCTYPE html>
<html lang="en">
<head>
<meta charset="utf-8">
<title>Brovexa Proposal Template</title>
<link rel="stylesheet" href="https://fonts.googleapis.com/css2?family=Arimo:wght@400;700&family=Montserrat:wght@400;500;600&display=swap">
<style>
  :root {
    --backdrop: #3b312c;
    --paper: #ececec;
    --charcoal: #2a292b;
    --green: #8aa83a;
    --green-deep: #5f9a34;
    --ink: #262626;
    --text-light: #f0f0f0;
  }
  * { box-sizing: border-box; margin: 0; padding: 0; }
  html, body {
    width: 1200px; height: 962px; overflow: hidden;
    background: var(--backdrop);
  }
  .sheet {
    position: absolute; top: 151px; width: 458px; height: 648px;
    background: var(--paper); overflow: hidden;
    box-shadow: 0 2px 8px rgba(0,0,0,.35);
  }
  .cover { left: 96px; font-family: "Arimo", Arial, sans-serif; }
  .page { left: 635px; font-family: "Montserrat", Helvetica, sans-serif; }

  .cover-art { position: absolute; inset: 0; }
  .headline {
    position: absolute; left: 65px; top: 74px;
    font-weight: 700; font-size: 37px; letter-spacing: -1px; line-height: 1;
    color: var(--text-light);
  }
  .offer {
    position: absolute; left: 65px; top: 136px;
    font-weight: 700; font-size: 35px; letter-spacing: -1px; line-height: 43px;
    color: var(--green);
  }
  .brand-cover { position: absolute; left: 108px; top: 400px; display: flex; align-items: center; gap: 14px; }
  .brand-mark { width: 58px; height: 58px; background: var(--green); }
  .brand-name {
    font-weight: 700; font-size: 38px; line-height: 1; color: var(--ink);
  }
  .brand-tag {
    font-size: 15px; letter-spacing: 1.5px; color: var(--ink); margin-top: 5px;
  }
  .contact {
    position: absolute; right: 200px; top: 584px; text-align: right;
    color: var(--ink); font-weight: 700;
  }
  .contact .phone { color: var(--green); font-size: 15px; font-weight: 400; line-height: 17px; }
  .contact .line { font-size: 7.5px; line-height: 13px; }
  .contact-divider {
    position: absolute; left: 284px; top: 592px; width: 1px; height: 34px; background: var(--ink);
  }
  .social { position: absolute; left: 303px; top: 600px; display: flex; gap: 14px; }
  .social span { width: 17px; height: 17px; border-radius: 50%; background: var(--green); }

  .brand-page { position: absolute; right: 44px; top: 28px; display: flex; align-items: center; gap: 8px; }
  .brand-page .brand-mark { width: 26px; height: 26px; }
  .brand-page .brand-name { font-family: "Montserrat", Helvetica, sans-serif; font-size: 16px; font-weight: 600; color: var(--green); }
  .brand-page .brand-tag { font-size: 6.5px; letter-spacing: .6px; margin-top: 2px; }
  .doc-title {
    position: absolute; left: 43px; top: 130px;
    font-size: 15.5px; font-weight: 500; letter-spacing: .9px; color: var(--green-deep);
  }
  .doc-subtitle {
    position: absolute; left: 43px; top: 154px;
    font-size: 9.5px; font-weight: 600; letter-spacing: .5px; color: var(--green);
  }
  .footer-bar {
    position: absolute; left: 0; top: 621px; width: 342px; height: 19px;
    background: var(--charcoal); color: var(--text-light);
    font-size: 8px; font-weight: 600; letter-spacing: .4px;
    display: flex; align-items: center; padding-left: 34px; gap: 9px;
  }
  .footer-bar .sep { width: 1px; height: 12px; background: var(--text-light); }
  .footer-mark { position: absolute; left: 352px; top: 606px; width: 24px; height: 24px; background: var(--green); }
  .page-tab {
    position: absolute; left: 383px; top: 606px; width: 75px; height: 23px;
    background: var(--green); color: #fff; font-size: 9.5px; font-weight: 600;
    display: flex; align-items: center; padding-left: 18px; gap: 8px;
  }
  .page-tab .sep { width: 1px; height: 11px; background: #fff; }
</style>
</head>
<body>
  <section class="sheet cover">
    <svg class="cover-art" width="458" height="648" viewBox="0 0 458 648">
      <polygon points="0,0 458,0 458,250 0,498" fill="var(--charcoal)"/>
      <polygon points="0,506 458,262 458,285 0,530" fill="var(--green)"/>
      <polygon points="97,388 182,351 182,480 97,500" fill="var(--paper)"/>
    </svg>
    <h1 class="headline">24/7 IT SUPPORT</h1>
    <p class="offer">NO LOCK<br>IN CONTRACTS</p>
    <div class="brand-cover">
      <div class="brand-mark"></div>
      <div>
        <div class="brand-name">Brovexa</div>
        <div class="brand-tag">CONSULTING&nbsp;&nbsp;SERVICES</div>
      </div>
    </div>
    <div class="contact">
      <div class="phone">1300 555 271</div>
      <div class="line">hello@brovexa.com.au</div>
      <div class="line">Level 8, 120 Harbour Lane, Geelong, Vic, 3220</div>
    </div>
    <div class="contact-divider"></div>
    <div class="social" aria-label="Social media links">
      <span></span><span></span><span></span><span></span><span></span>
    </div>
  </section>

  <section class="sheet page">
    <div class="brand-page">
      <div class="brand-mark"></div>
      <div>
        <div class="brand-name">Brovexa</div>
        <div class="brand-tag">CONSULTING&nbsp;&nbsp;SERVICES</div>
      </div>
    </div>
    <h2 class="doc-title">Title Of The Presentation</h2>
    <p class="doc-subtitle">add your subtitle goes here</p>
    <div class="footer-bar">
      <span>www.brovexa.com.au</span><span class="sep"></span><span>1300 555 271</span>
    </div>
    <div class="footer-mark"></div>
    <div class="page-tab"><span>Page</span><span class="sep"></span></div>
  </section>
</body>
</html>
```